Flyer-Design für Webinar zum Thema Elektrosmog etc.
Zielgruppe
Wir vertreiben Lösungen die Menschen vor schädlichem Elektrosmog, 5G, WLAN, Feinstaub, Erdstrahlung und Wasserverunreinigungen schützen. Unsere Zielgruppe sind umweltbewusste Menschen von 30 bis 80 Jahren, die wissen das die aktuelle Situation mit immer mehr strahlender Technologie kein Fortschritt mehr ist und die etwas dagegen tun wollen.
Ziel ist der Schutz der eigenen Familie in einem Rundum-Sorglos-Paket...
PS: Die Webseite auf der weitere Infos zu finden sind und in deren Look&Feel der Flyer designt werden soll heißt:
https://klarwerk-lebenshof.de/
Aufgabenstellung
A5-Quadrat 14,8 x 14,8 bzw. 15,0 x 15,0 mit Rand/Abschnitt/Vorgabe der Druckerei - Vorder und Rückseite
Design hochwertig im Auftritt des Flyers. Neugierig machen. Denke den Header der Webseite und diverse Bilder wie zum Beispiel die Fotos vom Feinstaub und vom Funk-Sendemasten auf der Webseite sollten als Eyecatcher mit eingebracht werden. Wichtig ist, dass der Flyer zum kostenlosen Fachwebinar einlädt um den Interessenten zu zeigen wie einfach man sich vor diesen vielschichtigen Gefahren schützen kann. Nicht zu viel Text = vielleicht die Quintessenz aus den einzelnen Kategorien...
Auf der Vorderseite das Wichtigste: Die Problematik (groß) und die Lösung: Die Einladung zum kostenlosen Webinar im Internet...
Auf der Rückseite weitere Infos zum Thema

```html
<!DOCTYPE html>
<html lang="de">
<head>
<meta charset="utf-8">
<title>Flyer Webinar – Vorder- und Rückseite</title>
<link rel="stylesheet" href="https://fonts.googleapis.com/css2?family=Heebo:wght@300;400;500;700;800;900&display=swap">
<style>
  :root{
    --stage:#e9e9e9;
    --paper:#f7f7f7;
    --navy:#0a2e52;
    --green:#9cc45c;
    --red:#d4202a;
    --white:#ffffff;
  }
  *{margin:0;padding:0;box-sizing:border-box}
  html,body{width:1200px;height:792px;overflow:hidden}
  body{background:var(--stage);font-family:"Heebo",sans-serif;position:relative}

  .flyer{position:absolute;top:163px;width:499px;height:497px;overflow:hidden;background:var(--paper)}
  .flyer--front{left:58px}
  .flyer--back{left:639px}

  /* front */
  .front-photo{position:absolute;left:12px;top:10px;width:475px;height:420px;
    background:linear-gradient(180deg,#6f8f4a 0%,#9fb6b8 18%,#7d98ac 45%,#8ea0ad 75%,#9aa8b0 100%)}
  .front-photo::after{content:"";position:absolute;right:0;top:0;width:45%;height:80%;
    background:linear-gradient(200deg,rgba(140,90,60,.75),rgba(180,130,100,.2) 70%,transparent)}
  .badge{position:absolute;border-radius:50%;background:var(--green);color:var(--white);
    text-align:center;display:flex;flex-direction:column;align-items:center;justify-content:center}
  .badge--gratis{left:-1px;top:31px;width:164px;height:164px;border:1px solid #7fae3f}
  .badge__flag{color:var(--red);font-weight:900;font-size:18px;letter-spacing:-.5px;margin-bottom:6px}
  .badge__invite{font-weight:300;font-size:15px;line-height:17px;letter-spacing:2px}
  .headline{position:absolute;left:0;width:499px;top:185px;text-align:center;color:#f2f2f2;
    font-weight:800;font-size:47px;line-height:48px;letter-spacing:-3px;text-transform:uppercase;
    text-shadow:0 1px 3px rgba(0,0,0,.15)}
  .headline span{display:block}
  .teaser{position:absolute;left:0;width:499px;top:340px;text-align:center;color:#f0f0f0;
    font-weight:300;font-size:14px;letter-spacing:6px}
  .teaser-dot{position:absolute;left:243px;top:367px;width:6px;height:6px;border-radius:50%;background:#e0e0e0}
  .wave{position:absolute;left:0;width:100%}
  .front-url{position:absolute;left:0;width:499px;top:432px;text-align:center;color:var(--white);
    font-weight:700;font-size:23px;letter-spacing:-.3px}

  /* back */
  .family-photo{position:absolute;left:0;top:0;width:499px;height:230px;
    background:linear-gradient(180deg,#ecebe7 0%,#e4ddd3 55%,#c9b39a 100%)}
  .badge--help{left:25px;top:-7px;width:124px;height:117px;font-size:12.5px;line-height:14px;font-weight:300}
  .badge--help strong{font-weight:700}
  .info{position:absolute;left:0;top:0;width:499px;height:377px}
  .info__text{position:absolute;left:30px;width:460px;text-align:center;color:var(--white)}
  .info__lead{top:183px;font-weight:300;font-size:11px}
  .info__threats{top:199px;font-weight:700;font-size:16.5px;line-height:18px;letter-spacing:-.2px}
  .info__topic{top:269px;font-weight:700;font-size:12.5px;text-decoration:underline;text-underline-offset:2px}
  .benefits{position:absolute;left:115px;top:289px;list-style:none;color:var(--white);font-weight:300;font-size:10.5px;line-height:17px}
  .benefits li{position:relative;padding-left:16px}
  .benefits svg{position:absolute;left:0;top:4px}
  .info__cta{top:333px;font-weight:300;font-size:10.5px}
  .info__cta em{font-style:normal;color:var(--red);font-weight:700}
  .info__url{top:347px;font-weight:700;font-size:16.5px}
  .imprint{position:absolute;left:9px;top:366px;transform:rotate(-90deg);transform-origin:0 0;
    width:140px;color:#dfe6ee;font-size:5.5px;line-height:7px;font-weight:400}
  .tile{position:absolute;top:385px;height:112px}
  .tile--mast{left:0;width:169px;background:linear-gradient(180deg,#5f8fb8 0%,#a9b9c4 55%,#d59a4a 100%)}
  .tile--strain{left:176px;width:144px;background:linear-gradient(135deg,#8e8e8e,#bdb6b0 60%,#8a8a8a)}
  .tile--traffic{left:328px;width:171px;background:linear-gradient(160deg,#3c4147,#8c8f92 55%,#c9c9c9)}
</style>
</head>
<body>

<section class="flyer flyer--front" aria-label="Vorderseite">
  <div class="front-photo" role="img" aria-label="Foto: Person trinkt klares Wasser aus den Händen an einem Bach"></div>
  <div class="badge badge--gratis">
    <span class="badge__flag">GRATIS!</span>
    <span class="badge__invite">Jetzt am<br>kostenlosen<br>Webinar<br>teilnehmen!</span>
  </div>
  <h1 class="headline"><span>Gesund leben,</span><span>trotz Mobilfunk,</span><span>5G und Feinstaub?</span></h1>
  <p class="teaser">WIE GEHT DAS?</p>
  <span class="teaser-dot"></span>
  <svg class="wave" style="top:300px" width="499" height="197" viewBox="0 0 499 197" aria-hidden="true">
    <path d="M0 103 C120 68 230 108 330 88 C410 72 460 40 499 20 L499 197 L0 197 Z" fill="var(--navy)"/>
    <path d="M0 103 C120 68 230 108 330 88 C410 72 460 40 499 20" fill="none" stroke="var(--green)" stroke-width="2.5"/>
  </svg>
  <p class="front-url">www.klarwerk-lebenshof.de</p>
</section>

<section class="flyer flyer--back" aria-label="Rückseite">
  <div class="family-photo" role="img" aria-label="Foto: lächelnde Familie aus drei Generationen"></div>
  <div class="badge badge--help">Wir helfen<br>Menschen,<br><strong>gesund zu<br>leben!</strong></div>
  <svg class="wave" style="top:95px" width="499" height="282" viewBox="0 0 499 282" aria-hidden="true">
    <path d="M0 120 C70 78 160 72 260 72 C360 72 430 50 499 0 L499 282 L0 282 Z" fill="var(--navy)"/>
    <path d="M0 120 C70 78 160 72 260 72 C360 72 430 50 499 0" fill="none" stroke="var(--green)" stroke-width="2.5"/>
  </svg>
  <div class="info">
    <p class="info__text info__lead">Schützen Sie sich und Ihre Familie vor</p>
    <p class="info__text info__threats">Elektrosmog - Mobilfunk - 5G<br>Feinstaub - Trinkwasserbelastungen<br>Störfelder wie Erdstrahlen &amp; Wasseradern</p>
    <p class="info__text info__topic">Was erfahren Sie im Experten-Webinar:</p>
    <ul class="benefits">
      <li><svg width="10" height="10" viewBox="0 0 10 10"><path d="M1 5 L4 9 L9 0" fill="none" stroke="var(--green)" stroke-width="2"/></svg>Wie Sie vorhandene Störfelder erkennen!</li>
      <li><svg width="10" height="10" viewBox="0 0 10 10"><path d="M1 5 L4 9 L9 0" fill="none" stroke="var(--green)" stroke-width="2"/></svg>Wie Sie diese negativen Einflüsse permanent abschalten!</li>
    </ul>
    <p class="info__text info__cta">Jetzt <em>HIER</em> zum kostenlosen Webinar anmelden:</p>
    <p class="info__text info__url">www.klarwerk-lebenshof.de</p>
    <p class="imprint">Verantwortlich im Sinne des LPrG:<br>Klarwerk Lebenshof - Jonas K. Wendel,<br>Lindenweg 7, 95100 Beispielstadt.</p>
  </div>
  <div class="tile tile--mast" role="img" aria-label="Foto: Funk-Sendemasten im Abendhimmel mit 5G-Schriftzug"></div>
  <div class="tile tile--strain" role="img" aria-label="Foto: Frau mit Kopfschmerzen beim Telefonieren mit dem Handy"></div>
  <div class="tile tile--traffic" role="img" aria-label="Foto: Autos im Stau mit Abgasen und Feinstaub"></div>
</section>

</body>
</html>
```